we need a homepage for a marketplace

We manage all projects using our ground-breaking platform Kelvrim Hub. You get access to 150+ partners in 70 countries, security, cost efficiency, technical skills, speed, 100% visibility and accountability.Kelvrim aims to help clients realize the full potential of their investments, provide a competitive price, establish the business need as a competitive advantage, and provide a strategic business asset that can facilitate growth.
Target Market(s)
Freelancers
Industry/Entity Type
Business Software
Number of Pages Required
1 page
Requirements
Must have
- Credentials -http://qabdel.example/freelancer/public
- Front :
- Client:
- Email id - tomasp@lurvantsystems.example
- Password - 908172
- Partner:
- Email id - dorian@lurvantsystems.example
- Password - 908172
- Project Manager:
- Email id - mirela@lurvantsystems.example
- Password - 908172
Nice to have
- It will be nice to have a creative design, and a outside the box look/feel

```html
<!DOCTYPE html>
<html lang="en">
<head>
<meta charset="utf-8">
<title>Kelvrim Hub – Home</title>
<link rel="stylesheet" href="https://fonts.googleapis.com/css2?family=Roboto:wght@400;500;700&family=Source+Sans+3:wght@400&display=swap">
<style>
  :root {
    --orange: #f7871c;
    --slate: #34495e;
    --ink: #222;
    --text: #3d3d3d;
    --header-bg: #f7f9fb;
    --section-bg: #f0f1f2;
    --white: #ffffff;
  }
  * { margin: 0; padding: 0; box-sizing: border-box; }
  html, body { width: 1200px; height: 940px; overflow: hidden; }
  body { position: relative; background: var(--white); font-family: "Roboto", sans-serif; }

  .site-header {
    position: absolute; top: 0; left: 0; width: 1200px; height: 80px;
    background: var(--white);
    border-bottom: 1px solid #d8dce0;
  }
  .site-header__inner {
    position: absolute; left: 130px; top: 0; width: 938px; height: 80px;
    background: var(--header-bg);
  }
  .brand {
    position: absolute; left: 0; top: 22px;
    display: flex; align-items: center; gap: 8px;
    font-family: "Roboto", sans-serif; font-weight: 500; font-size: 30px;
    color: var(--slate); letter-spacing: -0.5px;
  }
  .brand__dot { width: 12px; height: 12px; border-radius: 50%; background: var(--slate); }
  .main-nav {
    position: absolute; right: 0; top: 31px;
    display: flex; align-items: center; font-size: 12.5px; color: var(--ink);
  }
  .main-nav a { text-decoration: none; color: inherit; margin-left: 24px; line-height: 26px; }
  .main-nav a:first-child { margin-left: 0; }
  .main-nav .is-active {
    background: var(--orange); color: var(--white); font-weight: 700;
    padding: 0 14px; border-radius: 13px; margin-right: -14px;
  }

  .hero {
    position: absolute; top: 81px; left: 0; width: 1200px; height: 517px;
  }
  .hero__photo {
    position: absolute; inset: 0;
    background: linear-gradient(160deg, #4a525c 0%, #353e49 45%, #2c3744 100%);
  }
  .hero__content {
    position: absolute; left: 362px; top: 190px; width: 476px; height: 174px;
    border-top: 1px solid #e6e8ea; border-bottom: 1px solid #e6e8ea;
    text-align: center; color: var(--white);
  }
  .hero__title { margin-top: 24px; font-size: 29px; font-weight: 700; letter-spacing: 0.3px; }
  .hero__lead { margin-top: 12px; font-family: "Source Sans 3", sans-serif; font-size: 13px; }
  .hero__actions { margin-top: 21px; display: flex; justify-content: center; gap: 18px; }
  .btn {
    display: inline-block; height: 29px; line-height: 27px; border-radius: 15px;
    font-size: 11px; text-decoration: none; border: 1px solid transparent;
  }
  .btn--partner { width: 126px; background: var(--orange); color: var(--white); }
  .btn--project { width: 150px; border-color: var(--white); color: var(--white); }

  .intro {
    position: absolute; top: 598px; left: 0; width: 1200px; height: 308px;
    background: var(--section-bg); text-align: center;
  }
  .intro__title {
    margin-top: 38px; font-size: 27px; line-height: 35px; font-weight: 700; color: var(--slate);
  }
  .intro__text {
    margin: 33px auto 0; width: 940px;
    font-family: "Source Sans 3", sans-serif; font-size: 12px; line-height: 21.6px; color: var(--text);
  }
  .btn--start {
    margin-top: 30px; width: 132px; height: 31px; line-height: 31px; border-radius: 16px;
    background: var(--slate); color: var(--white); font-size: 14px; font-weight: 500;
  }

  .next-photo {
    position: absolute; top: 906px; left: 0; width: 1200px; height: 34px;
    background: linear-gradient(90deg, #e9e3da 0%, #d6c9bd 40%, #c9a59a 70%, #e1cfc6 100%);
  }
</style>
</head>
<body>
  <header class="site-header">
    <div class="site-header__inner">
      <div class="brand"><span class="brand__dot"></span>Kelvrim</div>
      <nav class="main-nav">
        <a href="#" class="is-active">Home</a>
        <a href="#" style="margin-left:27px">About Us</a>
        <a href="#">How it works</a>
        <a href="#">Partners</a>
        <a href="#">Browse Project Manager</a>
      </nav>
    </div>
  </header>

  <section class="hero">
    <div class="hero__photo" role="img" aria-label="Business people in a meeting over a laptop and printed charts, darkened"></div>
    <div class="hero__content">
      <h1 class="hero__title">JOIN WITH US AS A</h1>
      <p class="hero__lead">Lorem Ipsum is simply dummy text of the printing and typesetting industry.</p>
      <div class="hero__actions">
        <a href="#" class="btn btn--partner">Become a Partner</a>
        <a href="#" class="btn btn--project">POST YOUR PROJECT</a>
      </div>
    </div>
  </section>

  <section class="intro">
    <h2 class="intro__title">Growing Your Business<br>Doesn’t Have A Rocket Science For Us</h2>
    <p class="intro__text">Lorem ipsum dolor sit amet, consectetur adipiscing elit. Nulla sit amet ex vitae sapien placerat pretium. Aenean aliquam feugiat finibus. Class aptent taciti sociosqu ad litora torquent per conubia nostra, per inceptos himenaeos. In posuere porttitor lorem, a ullamcorper lectus mollis sagittis. Maecenas rutrum metus tincidunt felis sodales ultrices.Lorem ipsum dolor sit amet, consectetur adipiscing elit. Nulla sit amet ex vitae sapien placerat pretium. Aenean aliquam feugiat finibus. Class aptent taciti sociosqu ad litora torquent per conubia nostra, per inceptos .</p>
    <a href="#" class="btn btn--start">Get Start</a>
  </section>

  <div class="next-photo" role="img" aria-label="Photo of people collaborating at work, start of next section"></div>
</body>
</html>
```